New education centre needs a flyer design

We need a flyer design for this coming holiday program in science for students in primary school. Its a science program for 2 days in which experiments, applications will be conducted to teach a concept. I will attach what we will be doing but the description needs to be as brief as possible so that viewers who see it will be interested and call to find out more. I leave the design and colors to you but it has to be attractive and eye catching. Please see attach for information on details of the program as well as the logo of our education centre in Singapore.
Primary School Students and Parents
Education

```html
<!DOCTYPE html>
<html lang="en">
<head>
<meta charset="utf-8">
<title>Holiday Camp Flyer – Bright Path Academy</title>
<link href="https://fonts.googleapis.com/css2?family=Sniglet:wght@800&family=Lilita+One&family=Chewy&family=Mulish:wght@800;900&display=swap" rel="stylesheet">
<style>
  :root {
    --navy: #0f2a5c;
    --note-top: #fff27a;
    --note-bottom: #fbd84a;
    --headline-red: #e8202a;
    --alarm-blue: #1f6fd6;
    --camp-green: #2fa84f;
    --ink: #1a1a1a;
    --paper: #ffffff;
    --pin-red: #d8323f;
  }
  * { margin: 0; padding: 0; box-sizing: border-box; }
  html, body { width: 848px; height: 1200px; overflow: hidden; background: var(--paper); }
  .flyer {
    position: relative; width: 848px; height: 1200px; overflow: hidden;
    background: var(--paper);
    font-family: "Mulish", "Century Gothic", sans-serif;
    color: var(--ink);
  }
  .paint-wash {
    position: absolute; inset: 0;
    background:
      linear-gradient(115deg, rgba(120,200,240,.55) 0%, rgba(255,255,255,0) 22%),
      linear-gradient(200deg, rgba(240,110,160,.55) 0%, rgba(255,255,255,0) 30%),
      linear-gradient(20deg, rgba(110,200,120,.5) 0%, rgba(255,255,255,0) 25%),
      linear-gradient(160deg, rgba(255,255,255,0) 55%, rgba(250,170,90,.5) 80%, rgba(120,190,240,.45) 100%);
  }
  .band { position: absolute; left: 0; width: 848px; }
  .band--top { top: 0; height: 80px; }
  .band--bottom { bottom: 0; height: 90px; }

  .note {
    position: absolute; left: 45px; top: 78px; width: 752px; height: 834px;
    background: linear-gradient(170deg, var(--note-top) 0%, #fff06a 50%, var(--note-bottom) 100%);
    box-shadow: 8px 10px 16px rgba(0,0,0,.22);
  }
  .pin {
    position: absolute; left: 342px; top: -4px; width: 80px; height: 100px;
    background: radial-gradient(circle at 40% 35%, #f26a74 0%, var(--pin-red) 55%, #a41d28 100%);
    border-radius: 50% 50% 45% 45%;
  }
  .note__copy { position: absolute; left: 23px; top: 128px; width: 704px; }
  .lead, .intro, .details {
    font-weight: 900; font-size: 28px; line-height: 40px;
  }
  .headline {
    font-family: "Sniglet", "Comic Sans MS", cursive; font-weight: 800;
    font-size: 56px; line-height: 40px; letter-spacing: 0;
    color: var(--paper); -webkit-text-stroke: 3px var(--headline-red);
    text-shadow: 3px 3px 0 var(--headline-red);
  }
  .alarm {
    font-family: "Lilita One", sans-serif; font-style: italic; font-weight: 400;
    letter-spacing: 1px; color: var(--alarm-blue);
    -webkit-text-stroke: 1px var(--paper);
  }
  .camp {
    font-family: "Chewy", "Lilita One", cursive; font-size: 40px; line-height: 40px;
    color: var(--camp-green);
    -webkit-text-stroke: 1px var(--paper);
  }
  .intro { margin-top: 18px; }
  .details { margin-top: 30px; text-align: justify; text-indent: 24px; }

  .contact {
    position: absolute; left: 68px; top: 928px;
    font-style: normal; font-weight: 800; font-size: 19px; line-height: 28px; color: var(--ink);
  }
  .brand {
    position: absolute; left: 612px; top: 968px; width: 220px;
    text-align: center; color: var(--navy);
    font-weight: 900; font-size: 20px; line-height: 24px;
  }
  .brand__dot {
    display: block; width: 84px; height: 84px; margin: 0 auto 10px;
    border-radius: 50%; background: var(--navy);
  }
</style>
</head>
<body>
<main class="flyer">
  <div class="paint-wash" role="img" aria-label="Soft watercolour brush strokes in blue, pink, green and orange"></div>

  <svg class="band band--top" viewBox="0 0 848 80" preserveAspectRatio="none" aria-hidden="true">
    <path d="M0 0 H848 V40 C700 72 560 20 420 46 C280 72 140 30 0 58 Z" fill="var(--navy)"/>
    <path d="M0 58 C140 30 280 72 420 46 C560 20 700 72 848 40" stroke="#fff" stroke-width="4" fill="none"/>
  </svg>

  <section class="note">
    <div class="pin" role="img" aria-label="Red push pin holding the note"></div>
    <div class="note__copy">
      <p class="lead"><span class="headline">HOME ALONE?</span> Ever thought of making your very OWN <span class="alarm">BURGLAR ALARM</span> to feel safe and impress your family and friends?</p>
      <p class="intro">In our <span class="camp">holiday camp</span>, this is exactly what we are going to be doing!!</p>
      <p class="details">We are going to guide you to build unique items by discovering what electricity is all about in a fun and exciting way by touching base on lights, batteries, electrical circuits and more. Don’t wait any longer! Be prepared to let your creative juices flow and your imagination come alive by creating your very own personalized electrical items!</p>
    </div>
  </section>

  <address class="contact">
    Call us at 61234587 to reserve your places now.<br>
    Limited slots available.<br>
    Address:<br>
    58 Seabreeze Avenue<br>
    Singapore 428195<br>
    Email: hello@brightpathacademy.sg
  </address>

  <div class="brand">
    <span class="brand__dot"></span>
    Bright Path Academy
  </div>

  <svg class="band band--bottom" viewBox="0 0 848 90" preserveAspectRatio="none" aria-hidden="true">
    <path d="M0 30 C160 10 300 50 450 30 C600 10 720 40 848 22 V90 H0 Z" fill="var(--navy)"/>
    <path d="M0 30 C160 10 300 50 450 30 C600 10 720 40 848 22" stroke="#fff" stroke-width="4" fill="none"/>
  </svg>
</main>
</body>
</html>
```